Harrowgate Medical Imaging marketing poster

A poster to advertise our services. Something outstanding that catches the eye. Will be displayed at medical centres. Needs to advertise the following:
Opening hours - Mon-fri 8am-5:30pm Sat 8am-12:30
Services offered: Ultrasound, CT, Xray, Conebeam CT, Barium Studies, Injections and Biopsies, 3D/4D pregnancy scans.
We Bulk Bill concession card holders and under 18's
Locally owned and operated
www.harrowgatemedicalimaging.example.com.au
include contact details also Tel: 94638270 Fax: 9463 8291

```html
<!DOCTYPE html>
<html lang="en">
<head>
<meta charset="utf-8">
<title>Harrowgate Medical Imaging – Poster</title>
<link rel="stylesheet" href="https://fonts.googleapis.com/css2?family=Roboto+Condensed:wght@700&family=Questrial&family=Lato:wght@400;700&display=swap">
<style>
  :root {
    --green: #a9c200;
    --blue: #3ba4dc;
    --blue-dark: #2a86bd;
    --ink: #1e1e1e;
    --paper: #ffffff;
    --photo-light: #f6f1ec;
    --photo-warm: #e4d8cc;
    --photo-grey: #c9c6c2;
    --photo-screen: #4d5d72;
  }
  * { margin: 0; padding: 0; box-sizing: border-box; }
  html, body { width: 869px; height: 1200px; overflow: hidden; background: var(--paper); }
  .poster { position: relative; width: 869px; height: 1200px; background: var(--paper); font-family: "Lato", sans-serif; color: var(--ink); }

  .hero-photo {
    position: absolute; left: 0; top: 0; width: 869px; height: 643px;
    background:
      linear-gradient(180deg, rgba(255,255,255,1) 0%, rgba(255,255,255,0) 22%),
      linear-gradient(100deg, var(--photo-light) 0%, var(--photo-warm) 38%, var(--photo-screen) 62%, var(--photo-grey) 78%, var(--photo-light) 100%);
  }

  .brand {
    position: absolute; left: 0; right: 0; top: 34px; display: flex; align-items: center; justify-content: center; gap: 14px;
  }
  .brand-mark { width: 34px; height: 34px; border-radius: 50%; background: var(--blue); }
  .brand-name {
    font-family: "Lato", sans-serif; font-weight: 400; font-size: 30px; line-height: 1.1;
    color: var(--ink); letter-spacing: 0.5px;
  }

  .headline {
    position: absolute; left: 0; right: 0; top: 665px; text-align: center;
    font-family: "Roboto Condensed", sans-serif; font-weight: 700; font-size: 94px;
    line-height: 1; color: var(--green); letter-spacing: 1px;
  }
  .subhead {
    position: absolute; left: 0; right: 0; top: 768px; text-align: center;
    font-family: "Questrial", sans-serif; font-size: 52px; line-height: 1;
    color: var(--blue); letter-spacing: 0.5px;
  }

  .ribbon { position: absolute; left: 30px; top: 860px; width: 812px; height: 100px; }
  .ribbon-text {
    position: absolute; left: 68px; top: 860px; width: 719px; height: 70px;
    display: flex; align-items: center; justify-content: center;
    font-weight: 700; font-size: 21px; color: #fff; letter-spacing: 0.5px;
  }

  .services {
    position: absolute; left: 0; right: 0; top: 982px; text-align: center;
    font-weight: 700; font-size: 18.5px; line-height: 33px;
  }
  .services span { margin: 0 9px; }
  .services span::before { content: "•"; color: var(--green); margin-right: 3px; }

  .hours {
    position: absolute; left: 0; right: 0; top: 1056px; text-align: center; font-size: 22px; line-height: 28px;
  }
  .hours-label { color: var(--blue); font-weight: 700; font-size: 18px; }
  .hours-value { font-weight: 700; }

  .local-note {
    position: absolute; left: 0; right: 0; top: 1095px; text-align: center;
    font-weight: 700; font-size: 14px; line-height: 20px; letter-spacing: 2px;
    color: var(--green); text-transform: uppercase;
  }

  .contact-bar {
    position: absolute; left: 0; bottom: 0; width: 869px; height: 57px; background: var(--green);
    display: flex; align-items: center; justify-content: space-between; padding: 0 12px;
    color: #fff; font-weight: 700; font-size: 12.5px;
  }
  .contact-item { display: flex; align-items: center; gap: 5px; white-space: nowrap; }
  .contact-item svg { width: 14px; height: 14px; fill: var(--blue); }
</style>
</head>
<body>
<main class="poster">
  <div class="hero-photo" role="img" aria-label="Sonographer in a white blouse operating an ultrasound machine with a scan displayed on its monitor"></div>

  <div class="brand">
    <span class="brand-mark"></span>
    <span class="brand-name">HARROWGATE<br>MEDICAL IMAGING</span>
  </div>

  <h1 class="headline">QUALIFIED STAFF</h1>
  <p class="subhead">WITH EXPERTISE IN SERVICES</p>

  <svg class="ribbon" viewBox="0 0 812 100" aria-hidden="true">
    <polygon points="0,35 60,35 60,97 0,97 24,66" fill="var(--blue)"/>
    <polygon points="38,70 60,97 60,70" fill="var(--blue-dark)"/>
    <polygon points="812,35 752,35 752,97 812,97 788,66" fill="var(--blue)"/>
    <polygon points="774,70 752,97 752,70" fill="var(--blue-dark)"/>
    <rect x="38" y="0" width="719" height="70" fill="var(--blue)"/>
  </svg>
  <div class="ribbon-text">WE BULK BILL CONCESSION CARD HOLDERS AND UNDER 18'S</div>

  <div class="services">
    <div><span>Ultrasound</span><span>CT</span><span>Xray</span><span>Conebeam CT</span><span>Barium Studies</span></div>
    <div><span>3D/4D pregnancy scans</span><span>Injections and Biopsies</span></div>
  </div>

  <p class="hours"><span class="hours-label">Opening hours</span> - <span class="hours-value">Mon-fri 8am-5:30pm Sat 8am-12:30</span></p>

  <p class="local-note">Locally owned and operated</p>

  <footer class="contact-bar">
    <span class="contact-item">
      <svg viewBox="0 0 24 24"><path d="M6.6 10.8a15 15 0 0 0 6.6 6.6l2.2-2.2c.3-.3.7-.4 1-.2 1.1.4 2.3.6 3.6.6.6 0 1 .4 1 1V20c0 .6-.4 1-1 1A17 17 0 0 1 3 4c0-.6.4-1 1-1h3.5c.6 0 1 .4 1 1 0 1.3.2 2.5.6 3.6.1.3 0 .7-.2 1z"/></svg>
      Tel 08 9463 8270
    </span>
    <span class="contact-item">
      <svg viewBox="0 0 24 24"><path d="M6 2h12v6H6z M3 9h18v9h-3v4H6v-4H3z"/></svg>
      Fax 08 9463 8291
    </span>
    <span class="contact-item">
      <svg viewBox="0 0 24 24"><path d="M2 5h20v14H2z"/></svg>
      info@harrowgatemedicalimaging.example.com.au
    </span>
    <span class="contact-item">
      <svg viewBox="0 0 24 24"><circle cx="12" cy="12" r="10"/></svg>
      www.harrowgatemedicalimaging.example.com.au
    </span>
  </footer>
</main>
</body>
</html>
```